Psychotherapist need a business card with logo

I am a psychotherapist in need of a business card. The card must have:

Marisol Trevuneda
Psicoterapeuta
937 281 706

Psychologists use the greek letter psy, which is the psychologist symbol, but I would prefer something like a mandala, a graphic symbol, an iconic tree, nothing very usual, but something that shows confidence and trust.

Industry/Entity Type

Business

```html
<!DOCTYPE html>
<html lang="es">
<head>
<meta charset="UTF-8">
<title>Marisol Trevuneda · Psicoterapeuta</title>
<link rel="stylesheet" href="https://fonts.googleapis.com/css2?family=Poppins:wght@300;400;700&display=swap">
<style>
  :root {
    --backdrop: #3b3b3b;
    --paper: #ebe0cc;
    --paper-light: #f6f0e4;
    --paper-shade: #e2d4bb;
    --ink-brown: #9b5c24;
    --band-dark: #6e3a12;
    --band-light: #a8672c;
    --emblem-light: #d2a574;
    --emblem-mid: #b47a42;
    --emblem-dark: #8d5220;
  }
  * { box-sizing: border-box; margin: 0; padding: 0; }
  html, body {
    width: 1200px;
    height: 902px;
    overflow: hidden;
    background: var(--backdrop);
  }
  .stage {
    width: 1200px;
    height: 902px;
    display: flex;
    align-items: center;
    justify-content: center;
  }
  .business-card {
    position: relative;
    width: 470px;
    height: 805px;
    background:
      radial-gradient(ellipse at 30% 55%, rgba(255, 255, 255, 0.55), rgba(255, 255, 255, 0) 60%),
      linear-gradient(160deg, var(--paper-light) 0%, var(--paper) 55%, var(--paper-shade) 100%);
    display: flex;
    flex-direction: column;
    align-items: center;
    font-family: "Poppins", sans-serif;
    color: var(--ink-brown);
    box-shadow: 0 18px 40px rgba(0, 0, 0, 0.45);
  }
  .card-band {
    position: absolute;
    left: 0;
    width: 100%;
    height: 16px;
    background: linear-gradient(180deg, var(--band-light), var(--band-dark));
  }
  .card-band--top { top: 0; }
  .card-band--bottom { bottom: 0; }
  .tree-emblem {
    margin-top: 100px;
    width: 360px;
    height: 360px;
    border-radius: 50%;
    background: radial-gradient(circle at 50% 45%, var(--emblem-light) 0%, var(--emblem-mid) 60%, var(--emblem-dark) 100%);
    opacity: 0.8;
  }
  .holder-name {
    margin-top: 80px;
    font-weight: 700;
    font-size: 40px;
    letter-spacing: 0.5px;
    line-height: 1;
  }
  .holder-role {
    margin-top: 14px;
    font-weight: 300;
    font-size: 22px;
    letter-spacing: 2px;
    text-transform: uppercase;
  }
  .contact-box {
    margin-top: 16px;
    width: 400px;
    height: 62px;
    border: 1.5px solid var(--ink-brown);
    display: flex;
    align-items: center;
    padding-left: 22px;
    gap: 26px;
  }
  .phone-icon { width: 20px; height: 30px; }
  .phone-number {
    font-weight: 400;
    font-size: 28px;
    letter-spacing: 1.5px;
  }
</style>
</head>
<body>
<main class="stage">
  <article class="business-card">
    <div class="card-band card-band--top"></div>
    <div class="tree-emblem" role="img" aria-label="Emblema de árbol con ramas formando una copa circular"></div>
    <h1 class="holder-name">Marisol Trevuneda</h1>
    <p class="holder-role">Psicoterapeuta</p>
    <div class="contact-box">
      <svg class="phone-icon" viewBox="0 0 20 30" aria-hidden="true">
        <rect x="2" y="1.5" width="16" height="27" rx="3" fill="none" stroke="currentColor" stroke-width="2"/>
        <line x1="2" y1="23" x2="18" y2="23" stroke="currentColor" stroke-width="1.5"/>
        <circle cx="10" cy="26" r="1.2" fill="currentColor"/>
      </svg>
      <span class="phone-number">937 281 706</span>
    </div>
    <div class="card-band card-band--bottom"></div>
  </article>
</main>
</body>
</html>
```